Motivational Poster Design Project

I would like to create a poster with some of my favorite quotes to hang in my office. I did a similar project in 2012 and I've uploaded the top 2 designs so you can get a better idea of what I'm looking for. I will provide feedback on your design within 24 hours of receiving it.

The poster must contain the following quotes:

"You’re only given a little spark of madness. You mustn’t lose it.”
- Dorian Falkes

“The most contrarian thing of all is not to oppose the crowd but to think for yourself.”
- Miles Crand

"I constantly see people rise in life who are not the smartest, sometimes not even the most diligent, but they are learning machines. They go to bed every night a little wiser than they were when they got up and boy does that help, particularly when you have a long run ahead of you."
- Harvey Belcott

“In theory, there’s no difference between theory and practice. But, in practice, there is.”
- Kees R. T. Ter Hoogwater

"At the end of the day, a reactionary life is a normal life. One thing is consistent in every remarkable person: they decide to do something remarkable. Don’t let the world choose who you become."
- Darvesh Kulani

“It usually takes 3-4 months to try enough that you can do a proper 80/20 analysis, then two months to design systems to scale what *is* working.”
-Ned Gowlan

“Authority is 20 percent given, 80 percent taken.”
- Harold Finchamp

“Your actions are consistent with the way the world occurs to you.”
- Gustav Lemmke
Updates

Project Deadline Extended
Reason: I am going to be travelling with no access to internet until January 5th, 2015. I am extending the project deadline until 12/31/14 and I'll make a final decision during the 1st week of January.

Target Market(s)

Personal Project

Industry/Entity Type

Learning

Requirements
Must have
• The poster will be 24" high x 36" long and printed on canvas, so the image you create needs to have a resolution of at least 2700 x 3900.
Nice to have
• I don't have an exact vision for how the poster should look, so I am totally open to you using your creativity to develop, arrange and present the content as you'd like.
• That said, I would like an image (photo or posterized image) of the person being quoted along with each quote. I do not have specific images that I would like you to use, so you will need to find the images on your own. The images don't need to be perfect... I am more interested in the poster relating the essence of the quotes and the people being quoted than I am in perfect photographic images of the people being quoted.

```html
<!DOCTYPE html>
<html lang="en">
<head>
<meta charset="utf-8">
<title>Quotes Poster</title>
<link href="https://fonts.googleapis.com/css2?family=Delius&display=swap" rel="stylesheet">
<style>
  :root {
    --bg: #0b0b0b;
    --yellow: #f5a51b;
    --purple: #9a3fd8;
    --blue: #3b7de2;
    --red: #e8173d;
    --royal: #2e62d9;
    --orange: #f46a10;
    --green: #8fe61f;
    --lilac: #a04fd8;
    --quote-ink: #ffffff;
    --name-ink: #141414;
    --photo-light: #b9b9b9;
    --photo-dark: #3a3a3a;
  }
  * { margin: 0; padding: 0; box-sizing: border-box; }
  html, body { width: 830px; height: 1200px; overflow: hidden; background: var(--bg); }
  .poster {
    position: relative;
    width: 830px;
    height: 1200px;
    overflow: hidden;
    background: radial-gradient(ellipse at 50% 45%, #161616 0%, var(--bg) 70%);
    font-family: "Delius", cursive;
  }
  .quote-panel {
    position: absolute;
    z-index: 1;
    isolation: isolate;
    color: var(--quote-ink);
    font-size: 17px;
    line-height: 22px;
  }
  .quote-panel::before {
    content: "";
    position: absolute;
    inset: 0;
    background: var(--band);
    clip-path: polygon(1% 6%, 12% 0%, 40% 4%, 70% 0%, 99% 3%, 100% 45%, 98% 96%, 70% 100%, 35% 95%, 6% 100%, 0% 60%);
    z-index: -1;
  }
  .quote-panel blockquote { position: absolute; white-space: pre; }
  .quote-panel .name {
    position: absolute;
    color: var(--name-ink);
    font-size: 17px;
    line-height: 22px;
    white-space: nowrap;
  }
  .align-right blockquote { text-align: right; }

  .portrait {
    position: absolute;
    background: linear-gradient(160deg, var(--photo-light) 0%, #7a7a7a 45%, var(--photo-dark) 100%);
    z-index: 2;
  }

  /* panels */
  .p1 { --band: var(--yellow); left: 140px; top: 75px; width: 530px; height: 100px; }
  .p1 blockquote { left: 38px; top: 17px; }
  .p1 .name { left: 57px; top: 70px; }

  .p2 { --band: var(--purple); left: 171px; top: 207px; width: 586px; height: 104px; transform: rotate(-2deg); }
  .p2 blockquote { right: 145px; top: 19px; }
  .p2 .name { left: 275px; top: 74px; }

  .p3 { --band: var(--blue); left: 192px; top: 316px; width: 607px; height: 203px; transform: rotate(-3deg); }
  .p3 blockquote { left: 62px; top: 22px; font-size: 16.5px; line-height: 20px; }
  .p3 .name { left: 104px; top: 170px; }

  .p4 { --band: var(--red); left: 140px; top: 535px; width: 597px; height: 135px; }
  .p4 blockquote { right: 94px; top: 24px; line-height: 26px; }
  .p4 .name { right: 130px; top: 85px; }

  .p5 { --band: var(--royal); left: 166px; top: 664px; width: 664px; height: 156px; transform: rotate(-3deg); }
  .p5 blockquote { left: 24px; top: 18px; }
  .p5 .name { left: 67px; top: 118px; }

  .p6 { --band: var(--orange); left: 41px; top: 830px; width: 582px; height: 115px; }
  .p6 blockquote { right: 14px; top: 15px; line-height: 24px; }
  .p6 .name { left: 431px; top: 86px; }

  .p7 { --band: var(--green); left: 156px; top: 970px; width: 555px; height: 112px; transform: rotate(-2deg); }
  .p7 blockquote { left: 30px; top: 26px; }
  .p7 .name { left: 72px; top: 66px; }

  .p8 { --band: var(--lilac); left: 78px; top: 1080px; width: 560px; height: 98px; }
  .p8 blockquote { right: 18px; top: 11px; }
  .p8 .name { left: 375px; top: 63px; }

  /* portraits */
  .ph1 { left: 36px; top: 47px; width: 132px; height: 180px; }
  .ph2 { left: 622px; top: 156px; width: 130px; height: 155px; }
  .ph3 { left: 10px; top: 306px; width: 238px; height: 200px; }
  .ph4 { left: 650px; top: 488px; width: 115px; height: 172px; }
  .ph5 { left: 40px; top: 597px; width: 138px; height: 223px; }
  .ph6 { left: 662px; top: 711px; width: 128px; height: 200px; }
  .ph7 { left: 40px; top: 903px; width: 135px; height: 175px; }
  .ph8 { left: 645px; top: 1002px; width: 160px; height: 176px; }
</style>
</head>
<body>
<main class="poster">

  <figure class="quote-panel p1">
    <blockquote>You’re only given a little spark of madness.
 You mustn’t lose it</blockquote>
    <figcaption class="name">Dorian Falkes</figcaption>
  </figure>

  <figure class="quote-panel p2 align-right">
    <blockquote>The most contrarian thing of all is not to
oppose the crowd but to think for yourself</blockquote>
    <figcaption class="name">Miles Crand</figcaption>
  </figure>

  <figure class="quote-panel p3">
    <blockquote>I constantly see people rise in life who are
not the smartest, sometimes not even the most
diligent, but they are learning machines.
They go to bed every night a little wiser than
they were when they got up and boy does that
help, particularly when you have a long run ahead
of you</blockquote>
    <figcaption class="name">Harvey Belcott</figcaption>
  </figure>

  <figure class="quote-panel p4 align-right">
    <blockquote>In theory, there’s no difference between theory
and practice. But, in practice, there is</blockquote>
    <figcaption class="name">Kees R. T. Ter Hoogwater</figcaption>
  </figure>

  <figure class="quote-panel p5">
    <blockquote>At the end of the day, a reactionary life is a normal life.
One thing is consistent in every remarkable person:
they decide to do something remarkable.
Don’t let the world choose who you become</blockquote>
    <figcaption class="name">Darvesh Kulani</figcaption>
  </figure>

  <figure class="quote-panel p6 align-right">
    <blockquote>It usually takes 3-4 months to try enough that you can
do a proper 80/20 analysis, then two months to design
systems to scale what *is* working</blockquote>
    <figcaption class="name">Ned Gowlan</figcaption>
  </figure>

  <figure class="quote-panel p7">
    <blockquote>Authority is 20 percent given, 80 percent taken</blockquote>
    <figcaption class="name">Harold Finchamp</figcaption>
  </figure>

  <figure class="quote-panel p8 align-right">
    <blockquote>Your actions are consistent with the
way the world occurs to you</blockquote>
    <figcaption class="name">Gustav Lemmke</figcaption>
  </figure>

  <div class="portrait ph1" role="img" aria-label="Black and white portrait of Dorian Falkes, arms crossed"></div>
  <div class="portrait ph2" role="img" aria-label="Black and white portrait of Miles Crand"></div>
  <div class="portrait ph3" role="img" aria-label="Black and white portrait of Harvey Belcott in glasses"></div>
  <div class="portrait ph4" role="img" aria-label="Black and white portrait of Kees R. T. Ter Hoogwater"></div>
  <div class="portrait ph5" role="img" aria-label="Black and white portrait of Darvesh Kulani smiling"></div>
  <div class="portrait ph6" role="img" aria-label="Black and white portrait of Ned Gowlan"></div>
  <div class="portrait ph7" role="img" aria-label="Black and white portrait of Harold Finchamp"></div>
  <div class="portrait ph8" role="img" aria-label="Black and white portrait of Gustav Lemmke"></div>

</main>
</body>
</html>
```